Card Game Design - 5 Faces Only (Islamic Geometry Inspired)

The idea behind this project is to design a set a cards for a game. The game works as follows:

1 - Everyday you start with a deck of cards
2 - As the day progresses each card contains an action to perform
3 - If you perform that action, you move the card, face-up, to the pack of the deck
4 - If you do not perform that action, you flip the card over and place it at the back of the deck.
5 - At the end of the day, you review your deck.

The front of each card contains 3 major elements:

1 - Title
2 - Value - ie a number, score for completing the act
3 - An encouraging statement

The back of each card contains 3 elements:

1 - Title
2 - Value - ie a number, essentially a “minus” number
3 - A calligraphic symbol that will take-up of most of the card.

The back of the card is a simpler single design. The front of the card is slightly more complex. The front cards need to be of four types. The difference in types should preferably be in both color and design changes that indicate the four types.

Thus, the designer will be designing essentially 5 card faces. The back is the same for all designs, but the front four can either be variations in color / form or both.

The front facing cards are of the following types:

1 - Prayer - these are the cards that will reflect a prayer to be performed
2 - Day - these will be cards with actions to be performed on Monday, Thursday and Friday
3 - Awrād - activities that are to be performed on a daily basis
4 - Daily - activities that are to be performed on a daily basis

Overall Design Ethic

Modern board games have beautifully designed cards that are uniquely branded. The overall ethos of these cards are that they should reflect traditional Islamic art in nature. Think beautiful designed geometric patterns and calligraphy. If one can weave these design elements in a card face that is beautifully showcases the main elements - title, point and statement - that would be ideal.For this design project,

I am looking to get the 5 cards in PSDs ready for printing. I will add the front facing text and the text for the reverse except for the calligraphic panel that is linked below. Nevertheless, sample fonts and texts should be provided so that overall harmony with the design can be effectively assessed.

The calligraphic symbol for the back can be found here:

https://www.pelvarin-find.example/results?q=brush+script+panel&set=img&ref=A1b2C3d4E5f6G7h8

A circular version and square version that show in the display are very appealing. Other versions can be used if assessed to have a better fit for the design.

Alternatively, a calligraphic rendering of the phrase "Astaghfirullah" can also be used. Samples here:

https://www.pelvarin-find.example/results?q=ink+phrase+lettering&set=img&ref=H9i8J7k6L5m4N3o2

Sample Design Ethos

https://www.pelvarin-find.example/results?q=framed+panel&set=img&ref=P1q2R3s4T5u6V7w8

https://www.pelvarin-find.example/results?set=img&q=gilded+manuscript+borders&ref=X9y8Z7a6B5c4D3e2F1g0h9

https://www.pelvarin-find.example/results?set=img&q=ornate+tile+motifs&ref=J1k2L3m4N5o6P7q8R9s0#view=_

https://www.pelvarin-find.example/results?q=star+lattice+patterns&set=img&ref=T1u2V3w4X5y6Z7a8

Board Game Ethos

https://www.pelvarin-find.example/results?set=img&q=tabletop+card+layouts&ref=B1c2D3e4F5g6H7i8J9k0

Font styles to use
Serif
Sans Serif

Requirements
Must have
• Elegant, unified design.
• Must be aesthetically pleasing.
• Beautiful and vivid coloring without being gaudy.
Nice to have
• Meaningful symbolism.
• For example: Two small circles in each top corner of the card. One with a stylized representation of the Tolvenne and the other the Spire of the Keeper's hall in Madinah.
• See: https://www.quillmarsh-stock.example/browse/stone+cube+shrine?page=3&layout=vertical&licensed=true&filter=safe&origin=related_browse
• See: https://www.pelvarin-find.example/results?q=brenhollow+college&set=img&ref=Q1w2E3r4T5y6U7i8O9p0A1s2D3f4G5h6J7k8L9z0X1c2V3b4N5m6

```html
<!DOCTYPE html>
<html lang="ar" dir="ltr">
<head>
<meta charset="utf-8">
<title>Daily Deeds Card Set</title>
<link rel="stylesheet" href="https://fonts.googleapis.com/css2?family=Harmattan:wght@400;500&family=Tinos&display=swap">
<style>
  :root {
    --page: #ffffff;
    --card-cream: #f8dbb8;
    --frame-teal: #17a9aa;
    --frame-gold: #f2a93b;
    --frame-blue: #1f5fa8;
    --rosette: #f0b35a;
    --mandala: #f3c186;
    --prayer: #f06a2a;
    --day: #26897f;
    --awrad: #f39526;
    --daily: #1e6fc4;
    --back-navy: #0a1a4c;
    --back-deep: #040c2e;
    --back-gold: #f7b52c;
    --serif: "Tinos", "Times New Roman", serif;
    --arabic: "Harmattan", "Noto Naskh Arabic", sans-serif;
  }
  * { box-sizing: border-box; margin: 0; padding: 0; }
  html, body { width: 1200px; height: 742px; overflow: hidden; background: var(--page); }
  .deck { position: relative; width: 1200px; height: 742px; }

  .card {
    position: absolute;
    background: var(--card-cream);
    color: var(--accent);
  }
  .card--prayer { left: 59px;  top: 138px; width: 205px; height: 287px; --accent: var(--prayer); }
  .card--day    { left: 279px; top: 244px; width: 211px; height: 295px; --accent: var(--day); }
  .card--awrad  { left: 503px; top: 158px; width: 202px; height: 282px; --accent: var(--awrad); }
  .card--daily  { left: 717px; top: 271px; width: 208px; height: 290px; --accent: var(--daily); }
  .card--back   { left: 938px; top: 124px; width: 207px; height: 289px; background: radial-gradient(circle at 50% 50%, #16306e 0%, var(--back-navy) 45%, var(--back-deep) 100%); --accent: var(--back-gold); }

  .frame {
    position: absolute;
    inset: 6px;
    border: 8px solid var(--frame-teal);
    outline: 1.5px dotted var(--frame-gold);
    outline-offset: -5px;
  }
  .frame::after {
    content: "";
    position: absolute;
    inset: 2px;
    border: 1px solid var(--frame-blue);
    opacity: .35;
  }
  .rosette {
    position: absolute;
    width: 16px; height: 16px;
    border-radius: 50%;
    background: radial-gradient(circle, var(--frame-teal) 0 35%, var(--rosette) 36% 100%);
  }
  .rosette--tl { left: 2px;  top: 2px; }
  .rosette--tr { right: 2px; top: 2px; }
  .rosette--bl { left: 2px;  bottom: 2px; }
  .rosette--br { right: 2px; bottom: 2px; }

  .mandala {
    position: absolute;
    width: 34px; height: 34px;
    border-radius: 50%;
    background: radial-gradient(circle, #b9d3d0 0 12%, var(--mandala) 13% 70%, rgba(243,193,134,0) 72%);
    opacity: .75;
  }
  .mandala--tl { left: 17px;  top: 17px; }
  .mandala--tr { right: 17px; top: 17px; }
  .mandala--bl { left: 17px;  bottom: 17px; }
  .mandala--br { right: 17px; bottom: 17px; }

  .emblem {
    position: absolute;
    left: 50%;
    top: 14%;
    width: 86px;
    height: 27%;
    transform: translateX(-50%);
    border: 2px solid var(--accent);
    border-radius: 6px;
    background: rgba(255,255,255,.18);
  }

  .card-title {
    position: absolute;
    left: 0; right: 0;
    top: 41%;
    text-align: center;
    font-family: var(--arabic);
    font-weight: 500;
    font-size: 27px;
    line-height: 1.2;
    direction: rtl;
  }
  .card-value {
    position: absolute;
    left: 0; right: 0;
    top: 54%;
    text-align: center;
    font-family: var(--serif);
    font-size: 42px;
    line-height: 1;
  }
  .card-verse {
    position: absolute;
    left: 18%; right: 18%;
    top: 68.5%;
    text-align: center;
    font-family: var(--arabic);
    font-size: 12px;
    line-height: 1.6;
    direction: rtl;
  }

  .card--back .frame { outline-color: var(--back-gold); }
  .back-title {
    position: absolute;
    left: 0; right: 0;
    top: 11%;
    text-align: center;
    font-family: var(--arabic);
    font-size: 30px;
    color: var(--back-gold);
    direction: rtl;
  }
  .calligraphy-roundel {
    position: absolute;
    left: 50%;
    top: 27%;
    width: 138px;
    height: 138px;
    transform: translateX(-50%);
    border-radius: 50%;
    background: radial-gradient(circle, #1d2a5a 0 22%, #f1a02c 24% 30%, #6fb8a6 34% 46%, #f39a2a 52% 100%);
  }
  .back-value {
    position: absolute;
    left: 0; right: 0;
    top: 80%;
    text-align: center;
    font-family: var(--serif);
    font-weight: 700;
    font-size: 16px;
    color: var(--back-gold);
  }
</style>
</head>
<body>
<main class="deck">

  <article class="card card--prayer">
    <div class="frame"></div>
    <span class="rosette rosette--tl"></span><span class="rosette rosette--tr"></span>
    <span class="rosette rosette--bl"></span><span class="rosette rosette--br"></span>
    <span class="mandala mandala--tl" role="img" aria-label="Faint mandala ornament"></span>
    <span class="mandala mandala--tr" role="img" aria-label="Faint mandala ornament"></span>
    <span class="mandala mandala--bl" role="img" aria-label="Faint mandala ornament"></span>
    <span class="mandala mandala--br" role="img" aria-label="Faint mandala ornament"></span>
    <div class="emblem" role="img" aria-label="Line drawing of a domed mosque with two minarets"></div>
    <h2 class="card-title">صدقة</h2>
    <p class="card-value">1</p>
    <p class="card-verse">العطاء في الصدقة لا يقلل من ثروتك</p>
  </article>

  <article class="card card--day">
    <div class="frame"></div>
    <span class="rosette rosette--tl"></span><span class="rosette rosette--tr"></span>
    <span class="rosette rosette--bl"></span><span class="rosette rosette--br"></span>
    <span class="mandala mandala--tl" role="img" aria-label="Faint mandala ornament"></span>
    <span class="mandala mandala--tr" role="img" aria-label="Faint mandala ornament"></span>
    <span class="mandala mandala--bl" role="img" aria-label="Faint mandala ornament"></span>
    <span class="mandala mandala--br" role="img" aria-label="Faint mandala ornament"></span>
    <div class="emblem" role="img" aria-label="Line drawing of the Tolvenne shrine between two minarets"></div>
    <h2 class="card-title">صدقة</h2>
    <p class="card-value">2</p>
    <p class="card-verse">العطاء في الصدقة لا يقلل من ثروتك</p>
  </article>

  <article class="card card--awrad">
    <div class="frame"></div>
    <span class="rosette rosette--tl"></span><span class="rosette rosette--tr"></span>
    <span class="rosette rosette--bl"></span><span class="rosette rosette--br"></span>
    <span class="mandala mandala--tl" role="img" aria-label="Faint mandala ornament"></span>
    <span class="mandala mandala--tr" role="img" aria-label="Faint mandala ornament"></span>
    <span class="mandala mandala--bl" role="img" aria-label="Faint mandala ornament"></span>
    <span class="mandala mandala--br" role="img" aria-label="Faint mandala ornament"></span>
    <div class="emblem" role="img" aria-label="Line drawing of a kneeling figure in prayer on a mat"></div>
    <h2 class="card-title">فجر - عصر</h2>
    <p class="card-value">3</p>
    <p class="card-verse">من يصلي البردين (فجر وعصر) يدخل الجنة.</p>
  </article>

  <article class="card card--daily">
    <div class="frame"></div>
    <span class="rosette rosette--tl"></span><span class="rosette rosette--tr"></span>
    <span class="rosette rosette--bl"></span><span class="rosette rosette--br"></span>
    <span class="mandala mandala--tl" role="img" aria-label="Faint mandala ornament"></span>
    <span class="mandala mandala--tr" role="img" aria-label="Faint mandala ornament"></span>
    <span class="mandala mandala--bl" role="img" aria-label="Faint mandala ornament"></span>
    <span class="mandala mandala--br" role="img" aria-label="Faint mandala ornament"></span>
    <div class="emblem" role="img" aria-label="Line drawing of an open book on a folding stand"></div>
    <h2 class="card-title">صدقة</h2>
    <p class="card-value">4</p>
    <p class="card-verse">العطاء في الصدقة لا يقلل من ثروتك</p>
  </article>

  <article class="card card--back">
    <div class="frame"></div>
    <span class="rosette rosette--tl"></span><span class="rosette rosette--tr"></span>
    <span class="rosette rosette--bl"></span><span class="rosette rosette--br"></span>
    <h2 class="back-title">صلاة</h2>
    <div class="calligraphy-roundel" role="img" aria-label="Circular calligraphy panel in gold, orange and teal"></div>
    <p class="back-value">-3</p>
  </article>

</main>
</body>
</html>
```